business card deign

Logo needs the following on it.
1. attached logo
2. Tagline - "From icy coolers to party gear...we bring the good times!"
3. Name- Delia Fenwick, Founder and CPO
4. Address - 418 E. Harlow Avenue, Ste 2204, Tampa, FL. 33719
5. Phone - 720.555.0187

```html
<!DOCTYPE html>
<html lang="en">
<head>
<meta charset="UTF-8">
<title>Hopwell Business Card</title>
<link href="https://fonts.googleapis.com/css2?family=Ubuntu:wght@400;700&display=swap" rel="stylesheet">
<style>
  :root {
    --page-bg: #e9e6e1;
    --card-dark: #2a2a2a;
    --card-dark-deep: #1c1c1c;
    --card-light: #ffffff;
    --card-light-shade: #ececec;
    --ink: #111111;
    --ink-soft: #333333;
    --band: #0d0d0d;
    --band-text: #ffffff;
    --divider: #555555;
  }
  * { box-sizing: border-box; margin: 0; padding: 0; }
  html, body {
    width: 1200px; height: 900px; overflow: hidden;
    background: var(--page-bg);
    font-family: "Ubuntu", sans-serif;
  }
  .canvas { position: relative; width: 1200px; height: 900px; }

  .card {
    position: absolute; left: 300px; width: 600px; height: 343px;
    border-radius: 30px; overflow: hidden;
    box-shadow: 0 10px 28px rgba(0,0,0,0.22);
  }

  /* Back side */
  .card-back { top: 70px; background: var(--card-dark); }
  .back-pattern {
    position: absolute; inset: 0;
    background: linear-gradient(135deg, var(--card-dark) 0%, var(--card-dark-deep) 100%);
  }
  .back-brand {
    position: absolute; right: 44px; top: 150px;
    color: var(--card-light); font-weight: 700; font-size: 16px; letter-spacing: 3px;
  }

  /* Front side */
  .card-front {
    top: 487px;
    background: linear-gradient(120deg, var(--card-light-shade) 0%, var(--card-light) 45%, var(--card-light) 100%);
  }
  .brand-block {
    position: absolute; left: 40px; top: 60px; width: 230px; height: 180px;
    display: flex; flex-direction: column; align-items: center; justify-content: center; gap: 18px;
  }
  .brand-dot { width: 70px; height: 70px; border-radius: 50%; background: var(--ink); }
  .brand-name {
    font-weight: 700; font-size: 34px; letter-spacing: 10px; color: var(--ink);
  }
  .divider { position: absolute; left: 0; top: 0; }
  .contact {
    position: absolute; left: 320px; top: 70px; color: var(--ink-soft);
  }
  .contact-name { font-weight: 700; font-size: 20px; color: var(--ink); }
  .contact-title { font-size: 16px; margin-top: 2px; }
  .contact-list { list-style: none; margin-top: 18px; font-size: 15px; line-height: 1.3; }
  .contact-list li { display: flex; align-items: flex-start; gap: 8px; margin-bottom: 4px; }
  .contact-list svg { flex: none; margin-top: 2px; }

  .tagline-band {
    position: absolute; left: 0; right: 0; top: 262px; height: 34px;
    background: var(--band); color: var(--band-text);
    display: flex; align-items: center; justify-content: center;
    font-weight: 700; font-size: 17px; white-space: nowrap;
  }
</style>
</head>
<body>
<div class="canvas">

  <section class="card card-back">
    <div class="back-pattern" role="img" aria-label="Repeating tone-on-tone brand pattern across the dark card back"></div>
    <span class="back-brand">HOPWELL</span>
  </section>

  <section class="card card-front">
    <div class="brand-block">
      <span class="brand-dot"></span>
      <span class="brand-name">HOPWELL</span>
    </div>

    <svg class="divider" width="600" height="343" aria-hidden="true">
      <line x1="285" y1="40" x2="305" y2="235" stroke="var(--divider)" stroke-width="1"/>
    </svg>

    <div class="contact">
      <p class="contact-name">DELIA FENWICK</p>
      <p class="contact-title">Founder and CPO</p>
      <ul class="contact-list">
        <li>
          <svg width="14" height="14" viewBox="0 0 24 24" aria-hidden="true"><path fill="var(--ink)" d="M6.6 10.8a15.1 15.1 0 0 0 6.6 6.6l2.2-2.2a1 1 0 0 1 1-.25 11.4 11.4 0 0 0 3.6.57 1 1 0 0 1 1 1V20a1 1 0 0 1-1 1A17 17 0 0 1 3 4a1 1 0 0 1 1-1h3.5a1 1 0 0 1 1 1c0 1.25.2 2.450.57 3.57a1 1 0 0 1-.25 1z"/></svg>
          <span>720.555.0187</span>
        </li>
        <li>
          <svg width="14" height="16" viewBox="0 0 24 28" aria-hidden="true"><path fill="var(--ink)" d="M12 0a9 9 0 0 0-9 9c0 6.8 9 19 9 19s9-12.2 9-19a9 9 0 0 0-9-9zm0 12.5A3.5 3.5 0 1 1 12 5.5a3.5 3.5 0 0 1 0 7z"/></svg>
          <span>418 E. Harlow Avenue<br>Ste 2204, Tampa, FL. 33719</span>
        </li>
      </ul>
    </div>

    <div class="tagline-band">From icy coolers to party gear...we bring the good times!</div>
  </section>

</div>
</body>
</html>
```